" A empresa foi criada para comercializar e prestar serviços especializados em softwares voltados para infraestrutura de tecnologia. Nosso ramo de atuação será a venda e entrega de soluções para clientes que possuem infraestrutura de tecnologia própria (on-premisses) e clientes que não possuem infraestrutura, utilizando nuvens públicas como TNQ e Morvek. "

```html
<!DOCTYPE html>
<html lang="en">
<head>
<meta charset="utf-8">
<title>Veltrano Letterhead</title>
<link rel="stylesheet" href="https://fonts.googleapis.com/css2?family=Montserrat:wght@600&family=Open+Sans:wght@400;600&display=swap">
<style>
  :root{
    --backdrop:#e9ebee;
    --paper:#ffffff;
    --navy:#1d3b57;
    --teal:#2aa3c9;
    --teal-light:#8fd3ea;
    --ink:#4a4f55;
    --muted:#8a9097;
  }
  *{box-sizing:border-box;margin:0;padding:0}
  html,body{width:1200px;height:1200px;overflow:hidden;background:var(--backdrop)}
  body{display:flex;align-items:center;justify-content:center;font-family:"Open Sans",sans-serif;color:var(--ink)}
  .letterhead{
    position:relative;width:800px;height:1130px;background:var(--paper);
    box-shadow:0 6px 24px rgba(0,0,0,.12);padding:70px 72px 0 72px;
  }
  .brand{position:absolute;top:64px;right:72px;text-align:right}
  .brand-name{display:flex;align-items:center;gap:10px;justify-content:flex-end;
    font-family:"Montserrat",sans-serif;font-weight:600;font-size:34px;letter-spacing:2px;color:var(--navy)}
  .brand-name::before{content:"";width:22px;height:22px;background:var(--teal)}
  .brand-tagline{font-size:10px;color:var(--muted);letter-spacing:1.5px;margin-top:2px}
  .recipient{margin-top:30px;font-size:13px;line-height:1.55;font-weight:600;color:var(--navy);font-style:normal}
  .reference{position:absolute;top:215px;right:72px;text-align:right;font-size:11px;line-height:1.6;color:var(--muted)}
  .body-copy{margin-top:72px;font-size:12px;line-height:1.75;color:var(--ink)}
  .body-copy p{margin-bottom:18px;text-align:justify}
  .closing{margin-top:22px;font-size:12px}
  .signature{width:150px;height:64px;margin:10px 0 4px;background:linear-gradient(90deg,#f1f2f4,#e4e6e9);border-radius:4px}
  .signer{font-size:12px;font-weight:600;color:var(--navy)}
  .signer-role{font-size:11px;color:var(--muted)}
  .footer{position:absolute;left:72px;right:72px;bottom:70px}
  .footer-rule{height:3px;background:var(--teal);margin-bottom:14px}
  .contacts{display:flex;justify-content:space-between;font-size:11px;color:var(--muted)}
  .contact{display:flex;align-items:center;gap:7px}
  .contact svg{width:18px;height:18px}
  .footer-band{position:absolute;left:0;right:0;bottom:0;height:24px;
    background:linear-gradient(90deg,var(--teal),var(--teal-light))}
</style>
</head>
<body>
<main class="letterhead">
  <header class="brand">
    <div class="brand-name">VELTRANO</div>
    <div class="brand-tagline">Soluções em Infraestrutura</div>
  </header>

  <address class="recipient">
    To:<br>
    Mr. Daniel Ortega<br>
    Chief Executive Officer<br>
    Northwind Designs<br>
    Linden Walk<br>
    Corvale, Westmark 40917
  </address>

  <div class="reference">Reference: 001/1<br>16 March 2024</div>

  <section class="body-copy">
    <p>We are pleased to present our company, created to sell and deliver specialized software services for technology infrastructure. Our team supports clients with their own on-premises environments as well as those who rely fully on public clouds.</p>
    <p>Through partnerships with TNQ and Morvek, we design, migrate and manage workloads with care, keeping costs predictable and systems secure. Every project begins with a clear assessment of your current setup and business goals.</p>
    <p>We would welcome the opportunity to discuss how our solutions can support your next steps. Please feel free to contact us at any time.</p>
    <div class="closing">Sincerely,</div>
    <div class="signature" role="img" aria-label="Handwritten signature"></div>
    <div class="signer">Lucas Almeida</div>
    <div class="signer-role">Director</div>
  </section>

  <footer class="footer">
    <div class="footer-rule"></div>
    <div class="contacts">
      <span class="contact">
        <svg viewBox="0 0 24 24"><circle cx="12" cy="12" r="12" fill="var(--teal)"/><path d="M12 5.5a4 4 0 0 0-4 4c0 3 4 8 4 8s4-5 4-8a4 4 0 0 0-4-4zm0 5.5a1.5 1.5 0 1 1 0-3 1.5 1.5 0 0 1 0 3z" fill="#fff"/></svg>
        Rua das Acácias, 410
      </span>
      <span class="contact">
        <svg viewBox="0 0 24 24"><circle cx="12" cy="12" r="12" fill="var(--teal)"/><path d="M8.5 6.5l2 .2.8 2.5-1.3 1a7 7 0 0 0 3 3l1-1.3 2.5.8.2 2a1.5 1.5 0 0 1-1.6 1.3A9 9 0 0 1 7.2 8.1 1.5 1.5 0 0 1 8.5 6.5z" fill="#fff"/></svg>
        (11) 4820-7315
      </span>
      <span class="contact">
        <svg viewBox="0 0 24 24"><circle cx="12" cy="12" r="12" fill="var(--teal)"/><rect x="6" y="8" width="12" height="8.5" rx="1" fill="#fff"/><path d="M6.5 8.6l5.5 4.2 5.5-4.2" stroke="var(--teal)" stroke-width="1.2" fill="none"/></svg>
        contato@veltrano.com.br
      </span>
    </div>
  </footer>
  <div class="footer-band"></div>
</main>
</body>
</html>
```